ultra-minimalist business card

front (black background, matte):

samir t. kouri
writer | photographer
get@samirkouri.com

back (white background, matte):

a picture speaks a thousand words;
a word draws a thousand pictures.

www.samirkouri.com

all text should be small (white or silver - as long as it shows against the black - on the front; black or gray - as long as it shows against the white - on the back).

feel free to get creative in terms of arrangement, alignment, and font type, but remember, the overall style is minimalist, so nothing too fancy, please.

thanks.

```html
<!DOCTYPE html>
<html lang="en">
<head>
<meta charset="utf-8">
<title>samir t. kouri — business card</title>
<link rel="stylesheet" href="https://fonts.googleapis.com/css2?family=Questrial&display=swap">
<style>
  :root {
    --backdrop: #bcb9b5;
    --card-black: #050505;
    --card-white: #ecebe9;
    --ink-white: #f2f2f2;
    --ink-silver: #a9a9a9;
    --ink-gray: #6e6e6e;
    --ink-dark: #4a4a4a;
  }
  * { margin: 0; padding: 0; box-sizing: border-box; }
  html, body {
    width: 1200px;
    height: 1200px;
    overflow: hidden;
    background: var(--backdrop);
    font-family: "Questrial", "Century Gothic", sans-serif;
  }
  .sheet {
    width: 1200px;
    height: 1200px;
    display: flex;
    align-items: center;
    justify-content: center;
    gap: 80px;
  }
  .card {
    position: relative;
    width: 440px;
    height: 660px;
  }
  .card--front { background: var(--card-black); }
  .card--back { background: var(--card-white); }

  .identity {
    position: absolute;
    top: 42px;
    left: 40px;
  }
  .identity__name {
    font-size: 30px;
    letter-spacing: 1.5px;
    color: var(--ink-white);
    font-weight: 400;
    line-height: 1;
  }
  .identity__role {
    margin-top: 6px;
    margin-left: 40px;
    font-size: 17px;
    letter-spacing: 1.2px;
    color: var(--ink-silver);
    line-height: 1;
  }
  .contact {
    position: absolute;
    right: 36px;
    bottom: 36px;
    font-size: 19px;
    letter-spacing: 1px;
    line-height: 1;
  }
  .card--front .contact { color: var(--ink-white); }
  .card--back .contact { color: var(--ink-dark); }

  .quote {
    position: absolute;
    top: 270px;
    left: 84px;
    color: var(--ink-gray);
    font-size: 22px;
    letter-spacing: 1px;
    line-height: 1.2;
  }
  .quote__pair + .quote__pair { margin-top: 30px; }
  .quote__line { display: block; }
  .quote__line--indent { padding-left: 78px; }
</style>
</head>
<body>
  <main class="sheet">
    <section class="card card--front" aria-label="card front">
      <div class="identity">
        <h1 class="identity__name">samir t. kouri</h1>
        <p class="identity__role">writer | photographer</p>
      </div>
      <p class="contact">get@samirkouri.com</p>
    </section>

    <section class="card card--back" aria-label="card back">
      <div class="quote">
        <p class="quote__pair">
          <span class="quote__line">a picture speaks</span>
          <span class="quote__line quote__line--indent">a thousand words,</span>
        </p>
        <p class="quote__pair">
          <span class="quote__line">a word draws</span>
          <span class="quote__line quote__line--indent">a thousand pictures.</span>
        </p>
      </div>
      <p class="contact">get@samirkouri.com</p>
    </section>
  </main>
</body>
</html>
```